Small environmental consultancy needs a simple but professional web design

We are a boutique environmental consultancyand contracting business located in Margaret River in the South West of Western Australia.

We have two arms
1) Consulting which offers environmental planning, management and assessment services primarily to local government and the development industry.
2) Contracting which implements on site plans and on ground works primarily involving revegetation, bush regeneration and environmental weed control.

We need a simple yet professional web design within the wordpress platform that commmunicates professionalism, experience and technical expertise without appearing too corporate.

Something like this structure appeals:
http://verdantia.net.au/environment-services/
or
http://www.ridgefallenvironmental.com.au/index.php

(without the image gallery function)

Target Market(s)

Local Government Officers deciding on tenders;
Developers, Engineers, Town Planning consultants looking for environmental expertise

Industry/Entity Type

Business

Number of Pages Required

5+ page

Font styles to use
Sans Serif

Colors
33a6d7
9bcb3c

Requirements
Must have
• Pages required include:
• Home
• Environmental Planning and Management
• Revegetation and Regeneration Implementation (This page can mirror the Environmental Planning and Management page exactly in structure but with different text and images)
• About Us (I think that this page can be relatively simple and generic)
• Contact (I think that this page can be very simple and generic)
Nice to have
• An ability to start out basic and quicikly establish a website presence and then build in additional drop downs and pages over time.
Should not have
• It does not need a photo gallery page;
• It does not need a major amount of space dedicated to social media and blogs etc as this is not currently particularly active area for us

```html
<!DOCTYPE html>
<html lang="en">
<head>
<meta charset="utf-8">
<title>Karri Landcare — Contact</title>
<link href="https://fonts.googleapis.com/css2?family=PT+Sans:wght@400;700&family=Questrial&display=swap" rel="stylesheet">
<style>
  :root {
    --backdrop: #d3d4d6;
    --page: #ffffff;
    --brand-brown: #7e5222;
    --nav-active: #a0522d;
    --nav-text: #3a3a3a;
    --leaf-green: #9bcb3c;
    --field-border: #cfe09a;
    --heading: #2f2f33;
    --muted: #8a8a8a;
    --body-text: #222222;
    --map-water: #93b6e3;
    --map-park: #b6d69a;
    --map-land: #e9e6dc;
    --map-town: #e8d2c6;
  }
  * { margin: 0; padding: 0; box-sizing: border-box; }
  html, body { width: 1200px; height: 1000px; overflow: hidden; }
  body { background: var(--backdrop); font-family: "PT Sans", sans-serif; position: relative; }

  .site {
    position: absolute; left: 113px; top: 79px; width: 973px; height: 763px;
    background: var(--page); box-shadow: 0 2px 12px rgba(0,0,0,0.12);
  }
  .site-header { position: absolute; left: 0; top: 0; width: 100%; height: 61px; }
  .brand { position: absolute; left: 139px; top: 12px; height: 40px; display: flex; align-items: center; }
  .brand-mark { width: 36px; height: 36px; border-radius: 50%; background: var(--leaf-green); margin-right: 14px; }
  .brand-name {
    font-family: "PT Sans", sans-serif; font-weight: 400; font-size: 26px;
    color: var(--brand-brown); line-height: 1; white-space: nowrap;
  }
  .main-nav { position: absolute; top: 36px; left: 0; width: 100%; font-family: "Questrial", sans-serif; font-size: 6.2px; color: var(--nav-text); }
  .main-nav a { position: absolute; color: inherit; text-decoration: none; white-space: nowrap; }
  .main-nav a.is-current { color: var(--nav-active); }

  .location-map {
    position: absolute; left: 0; top: 61px; width: 100%; height: 318px;
    background: linear-gradient(90deg, var(--map-water) 0%, var(--map-water) 15%, var(--map-park) 20%, var(--map-land) 30%, var(--map-town) 45%, var(--map-town) 68%, var(--map-park) 78%, var(--map-land) 90%, var(--map-park) 100%);
  }

  .section-title {
    position: absolute; font-size: 18px; font-weight: 700; color: var(--heading);
    padding-left: 9px; border-left: 4px solid var(--leaf-green); line-height: 18px;
  }
  .contact-detail { position: absolute; left: 195px; top: 444px; font-size: 7px; line-height: 11.5px; color: var(--body-text); }
  .contact-detail dt { display: inline; color: var(--leaf-green); }
  .contact-detail dd { display: inline; }

  .field {
    position: absolute; border: 1px solid var(--field-border); background: #fff;
    font-family: "PT Sans", sans-serif; font-size: 7px; color: var(--muted); padding: 8px 9px;
  }
  .submit-btn {
    position: absolute; left: 445px; top: 608px; width: 34px; height: 14px;
    background: var(--leaf-green); color: #fff; font-size: 7px; text-align: center; line-height: 14px;
  }
  .form-note { position: absolute; left: 486px; top: 610px; font-size: 6.8px; color: var(--muted); }

  .site-footer { position: absolute; left: 0; top: 714px; width: 100%; height: 49px; background: var(--brand-brown); color: #fff; }
  .copyright { position: absolute; left: 195px; top: 20px; font-size: 6.8px; }
  .social-links { position: absolute; left: 699px; top: 21px; display: flex; gap: 9px; }
  .social-links span { width: 8px; height: 8px; border-radius: 50%; background: #fff; }
</style>
</head>
<body>
  <div class="site">
    <header class="site-header">
      <div class="brand">
        <span class="brand-mark"></span>
        <span class="brand-name">Karri Landcare</span>
      </div>
      <nav class="main-nav">
        <a class="is-current" style="left:436px">Home</a>
        <a style="left:479px">Environmental Planning and Management</a>
        <a style="left:617px">Revegetation and Regeneration Implementation</a>
        <a style="left:771px">About Us</a>
        <a style="left:821px">Contact</a>
      </nav>
    </header>

    <div class="location-map" role="img" aria-label="Street map of the town and surrounding coast, reserves and roads showing the office location"></div>

    <h2 class="section-title" style="left:195px; top:414px;">CONTACT DETAIL</h2>
    <dl class="contact-detail">
      <div><dt>Address: </dt><dd>Adress</dd></div>
      <div><dt>Mobile: </dt><dd>0000 000 000</dd></div>
      <div><dt>E-mail: </dt><dd>info@example.org</dd></div>
    </dl>

    <h2 class="section-title" style="left:445px; top:414px;">CONTACT FORM</h2>
    <div class="field" style="left:445px; top:449px; width:334px; height:26px;">Name*</div>
    <div class="field" style="left:445px; top:478px; width:167px; height:26px;">Email*</div>
    <div class="field" style="left:617px; top:478px; width:162px; height:26px;">Phone</div>
    <div class="field" style="left:445px; top:509px; width:334px; height:92px;">Message*</div>
    <div class="submit-btn">Submit</div>
    <div class="form-note">*Required fields</div>

    <footer class="site-footer">
      <p class="copyright">© Copyright 2014 by Karri Landcare. All Rights Reserved.</p>
      <div class="social-links"><span></span><span></span><span></span><span></span><span></span></div>
    </footer>
  </div>
</body>
</html>
```